Rock Concert Ticket

Invitation for a 50th birthday party in the form of a ticket to a rock concert -
think Knives 'n Tulips, OX/EV, Tumbling Pebbles, The Brawl, Tin Balloon etc.
Design should be very rock n roll with album cover type feel. Needs to reference 50 and include information like venue, date, dress code, rsvp etc. Invitation to be distributed electronically rather than hard copy.

Reason: Deadline has been extended to allow for some slight changes to 2-3 of the designs that I have narrowed it down to. I contacted the designers directly with feedback so you know who you are. Thanks

```html
<!DOCTYPE html>
<html lang="en">
<head>
<meta charset="utf-8">
<title>Ray's 50 Year Tour – Invitation Ticket</title>
<link rel="stylesheet" href="https://fonts.googleapis.com/css2?family=Special+Elite&family=Courier+Prime&family=Cabin+Sketch:wght@400&family=Anton&display=swap">
<style>
  :root {
    --page: #ffffff;
    --ink: #1a1a1a;
    --frame: #222222;
    --stage-light: #f4f6f9;
    --stage-mid: #d9dee6;
    --stage-dark: #aeb6c2;
  }
  * { margin: 0; padding: 0; box-sizing: border-box; }
  html, body {
    width: 1200px;
    height: 848px;
    overflow: hidden;
    background: var(--page);
  }
  .canvas {
    position: relative;
    width: 1200px;
    height: 848px;
  }
  .ticket {
    position: absolute;
    left: 63px;
    top: 161px;
    width: 1039px;
    height: 463px;
    border: 2px solid var(--frame);
    overflow: hidden;
    color: var(--ink);
  }
  .stage-photo {
    position: absolute;
    inset: 0;
    background:
      radial-gradient(ellipse at 28% 20%, var(--stage-light) 0%, rgba(244,246,249,0) 55%),
      linear-gradient(180deg, var(--stage-light) 0%, var(--stage-mid) 50%, var(--stage-dark) 72%, var(--stage-light) 100%);
    opacity: 0.85;
  }
  .stub-divider {
    position: absolute;
    left: 763px;
    top: 0;
    height: 100%;
    border-left: 3px dashed var(--frame);
  }
  .line {
    position: absolute;
    left: 0;
    width: 760px;
    text-align: center;
    white-space: nowrap;
  }
  .typewriter { font-family: "Courier Prime", "Courier New", monospace; font-size: 28px; }
  .distressed { font-family: "Special Elite", "Courier New", monospace; }
  .guests { top: 52px; font-size: 42px; letter-spacing: 1px; }
  .intro { top: 10px; }
  .entry { top: 108px; }
  .tour-title { top: 142px; font-size: 66px; letter-spacing: 1px; font-weight: bold; -webkit-text-stroke: 1.5px var(--ink); }
  .night { top: 228px; }
  .venue { top: 262px; font-family: "Cabin Sketch", "Comic Sans MS", cursive; font-size: 74px; }
  .date { top: 340px; font-family: "Anton", "Impact", sans-serif; font-size: 52px; letter-spacing: 1px; }
  .dress { top: 410px; }
  .date-vertical {
    position: absolute;
    left: 722px;
    top: 445px;
    transform: rotate(-90deg);
    transform-origin: left top;
    font-family: "Courier Prime", "Courier New", monospace;
    font-size: 28px;
    letter-spacing: 1px;
    white-space: nowrap;
  }
  .stub {
    position: absolute;
    left: 767px;
    top: 0;
    width: 270px;
    height: 100%;
    text-align: center;
    font-family: "Courier Prime", "Courier New", monospace;
  }
  .rsvp { position: absolute; left: 0; right: 0; top: 66px; font-size: 46px; letter-spacing: 2px; }
  .confirm { position: absolute; left: 0; right: 0; top: 182px; font-size: 18px; line-height: 25px; }
  .phone { position: absolute; left: 0; right: 0; top: 262px; font-size: 28px; letter-spacing: 1px; }
  .quote { position: absolute; left: 0; right: 0; top: 338px; font-size: 18px; line-height: 25px; }
</style>
</head>
<body>
<div class="canvas">
  <section class="ticket">
    <div class="stage-photo" role="img" aria-label="Faded photograph of a concert stage with lighting rigs and equipment"></div>

    <p class="line typewriter intro">This ticket entitles</p>
    <p class="line distressed guests">MAYA &amp; TOM</p>
    <p class="line typewriter entry">Exclusive entry to</p>
    <h1 class="line distressed tour-title">RAY'S 50 YEAR TOUR</h1>
    <p class="line typewriter night">One Night Only At</p>
    <p class="line venue">The Venue</p>
    <p class="line date">9th September 2014</p>
    <p class="line typewriter dress">Dress To Rock</p>

    <p class="date-vertical">09 09 2014</p>
    <div class="stub-divider"></div>

    <aside class="stub">
      <p class="rsvp">RSVP</p>
      <p class="confirm">To confirm your entry<br>text or call</p>
      <p class="phone">07700900123</p>
      <p class="quote">quoting your name<br>and number of<br>attendees</p>
    </aside>
  </section>
</div>
</body>
</html>
```